Book Cover Design - "Lanterns Seldom Wander"

Looking for an eye-catching but professional book cover.

This book is designed to help people figure out why they hate their job and what to do about it.

The audience for this book is 18-35 year olds who feel stuck in their current roles. The theory here is that people often wind up in a job they don't love, then settle because they don't realize they can make things better.

The writer's style is clever and balances humor with practical advice.

```html
<!DOCTYPE html>
<html lang="en">
<head>
<meta charset="utf-8">
<title>Lanterns Seldom Wander</title>
<link rel="stylesheet" href="https://fonts.googleapis.com/css2?family=Arimo:wght@700&display=swap">
<style>
  :root {
    --rust: #8a2c12;
    --rust-dark: #6e220d;
    --band: #000000;
    --ground: #1c0e08;
    --ground-warm: #3a1a0c;
    --ink: #ffffff;
  }
  html, body {
    margin: 0;
    padding: 0;
    width: 800px;
    height: 1200px;
    overflow: hidden;
    background: var(--ground);
  }
  .cover {
    position: relative;
    width: 800px;
    height: 1200px;
    overflow: hidden;
    background:
      radial-gradient(ellipse at 70% 30%, var(--ground-warm) 0%, transparent 55%),
      radial-gradient(ellipse at 40% 80%, var(--ground-warm) 0%, transparent 50%),
      var(--ground);
  }
  .figure-strip {
    position: absolute;
    left: 0;
    top: 0;
    width: 258px;
    height: 1200px;
    background: linear-gradient(180deg, var(--rust) 0%, var(--rust-dark) 50%, var(--rust) 100%);
  }
  .divider-band {
    position: absolute;
    left: 258px;
    top: 0;
    width: 72px;
    height: 1200px;
    background: var(--band);
  }
  .title {
    position: absolute;
    left: 0;
    top: 1200px;
    width: 1200px;
    height: 800px;
    margin: 0;
    transform-origin: 0 0;
    transform: rotate(-90deg);
    font-family: "Arimo", Arial, sans-serif;
    font-weight: 700;
    font-size: 132px;
    line-height: 96px;
    color: var(--ink);
    letter-spacing: 0.3em;
    white-space: nowrap;
  }
  .title-line {
    position: absolute;
    right: calc(25px - 0.3em);
    display: block;
  }
  .line-one { top: 302px; }
  .line-two { top: 458px; }
  .line-three { top: 620px; }
</style>
</head>
<body>
  <main class="cover">
    <div class="figure-strip" role="img" aria-label="Row of green pictogram figures with crossed-out eyes and one alert blue figure standing among them"></div>
    <div class="divider-band"></div>
    <h1 class="title">
      <span class="title-line line-one">LANTERNS</span>
      <span class="title-line line-two">SELDOM</span>
      <span class="title-line line-three">WANDER</span>
    </h1>
  </main>
</body>
</html>
```